Site Design - PSD Only - festival management

We are looking for a final design for our B2B marketplace. The project is a social commerce platform managing the application and transaction process for festivals and local events. The site design should be based on either Bootstrap or Zurb Foundation. We will provide logos and example images.

Two of the most critical pages will be the home page and the search interface, as well several dashboards. Beyond that, most of the pages will be standard forms and other typical pages that drop into the general site theme. The design tends towards minimalism to simplify the UX and speed up the interface. It incorporates elements from the the following websites. Although the wireframes may lift design elements directly from some of these sites, we are looking for a design that incorporates them more as inspiration.

brivel.co - good example of minimalist structure on internal pages
tovemix.com - some similarities on search pages, etc.
quenlar.com - nice simple layout for features on home and internal pages
mossbarrels.com - nice alternative to standard bootstrap template
Updates

We're nearing the end of this project.  I've received some good submissions , but they are all variations on the exact same theme.  I would still like to see something that doesn't look like a bootstrap template.  I suggested the following idea to a few of the submitters, but now I am adding it to the main project description in hopes of stoking the engine.

The idea I had is for something a little less "bootstrappy" riffs on the design at mossbarrels.com with a flat background color that nicely offsets the blue in the logo. Rather than pulling in a stock image I thought about creating a derivation of the iconic Harrowmere poster, perhaps with vendor tents as tuning pegs and a silhouette of people on the neck. Just throwing that out there. 

I'm not a designer, though, so here's hoping we can see some different ideas while the project is still open.

Thanks.

Target Market(s)

Target market: Festival and event organizers; event participants including exhibitors, vendors, musicians, authors, volunteers, etc.

Industry/Entity Type

Festival

Requirements
Must have
• Home page, Search page, User dash, Organization dash, Event dash, Features, FAQ, various forms
Nice to have
• Would like to see some alternative designs to the standard bootstrap templates...creativity is encouraged.
Should not have
• Should not look like it was pulled off of the shelf.

```html
<!DOCTYPE html>
<html lang="en">
<head>
<meta charset="utf-8">
<title>Velunda – Festival Management</title>
<link rel="stylesheet" href="https://fonts.googleapis.com/css2?family=Roboto:wght@300;400;500&family=Signika:wght@600;700&display=swap">
<style>
  :root {
    --blue: #1f80c9;
    --blue-link: #2a8ad0;
    --ink: #111;
    --grey-text: #555;
    --tab-dark: #333;
    --hero-bg: #000;
    --grid-line: #e2e2e2;
    --footer-bg: #3b3b3b;
    --footer-bottom: #272727;
    --footer-text: #d0d0d0;
  }
  * { box-sizing: border-box; }
  html, body { margin: 0; padding: 0; }
  body {
    width: 1200px; height: 1055px; overflow: hidden; position: relative;
    background: #fff; font-family: "Roboto", Arial, sans-serif; color: var(--ink);
  }
  .abs { position: absolute; }

  /* Header */
  .site-header { position: absolute; left: 0; top: 0; width: 1200px; height: 83px; }
  .brand { left: 141px; top: 20px; display: flex; align-items: center; gap: 10px; }
  .brand-mark { width: 48px; height: 48px; border-radius: 50%; background: var(--blue); }
  .brand-name { font-family: "Roboto", sans-serif; font-weight: 500; font-size: 19px; letter-spacing: 1px; color: #555; }
  .action-tabs { left: 296px; top: 36px; display: flex; }
  .action-tab {
    width: 90px; height: 15px; margin-right: -4px; color: #fff; font-size: 11px; line-height: 15px;
    text-align: center; clip-path: polygon(6px 0, 100% 0, calc(100% - 6px) 100%, 0 100%); background: var(--tab-dark);
  }
  .action-tab--primary { background: var(--blue); }
  .action-note { left: 296px; top: 52px; width: 82px; text-align: center; font-size: 10.5px; line-height: 11px; color: #333; }
  .search-box { left: 785px; top: 11px; width: 132px; height: 17px; background: #eee; border: 1px solid #ddd; }
  .social-square { width: 17px; height: 17px; border-radius: 2px; }
  .header-social { left: 923px; top: 11px; display: flex; gap: 5px; }
  .account-links { left: 977px; top: 12px; font-size: 11.5px; }
  .account-links a { text-decoration: none; }
  .account-links .register { color: var(--blue-link); }
  .account-links .login { color: #111; }
  .main-nav { right: 141px; top: 37px; display: flex; gap: 25px; font-size: 13px; color: #444; }

  /* Hero */
  .hero { left: 0; top: 83px; width: 1200px; height: 367px; background: var(--hero-bg); border-bottom: 3px solid var(--blue); }
  .hero-art {
    position: absolute; left: 527px; top: 0; width: 515px; height: 364px;
    background: radial-gradient(ellipse at 65% 45%, #f4f4f6 0 18%, #2a4fa8 32%, #0f1d45 58%, #000 80%);
  }
  .hero-title { left: 140px; top: 77px; font-family: "Signika", sans-serif; font-weight: 700; font-size: 56px; line-height: 1; color: #fff; margin: 0; }
  .hero-lead { left: 140px; top: 142px; width: 330px; font-family: "Signika", sans-serif; font-weight: 600; font-size: 19px; line-height: 24px; color: #fff; margin: 0; }
  .hero-cta {
    left: 140px; top: 229px; width: 166px; height: 33px; padding-left: 20px; line-height: 33px;
    background: var(--blue); color: #fff; font-size: 20px; clip-path: polygon(0 0, 100% 0, 83% 100%, 0 100%);
  }
  .slider-tab {
    left: 549px; top: 341px; width: 101px; height: 26px; background: var(--blue);
    clip-path: polygon(0 0, 100% 0, 88% 100%, 12% 100%); display: flex; justify-content: center; gap: 5px; padding-top: 8px;
  }
  .slider-dot { width: 11px; height: 11px; border-radius: 50%; background: #9cc6e8; }
  .slider-dot--active { background: #fff; }

  /* Features */
  .feature-grid {
    left: 140px; top: 489px; width: 919px; height: 337px; border: 1px solid var(--grid-line);
    display: grid; grid-template-columns: repeat(3, 1fr); grid-template-rows: repeat(2, 1fr);
  }
  .feature { border-right: 1px solid var(--grid-line); border-bottom: 1px solid var(--grid-line); text-align: center; padding-top: 30px; }
  .feature:nth-child(3n) { border-right: 0; }
  .feature:nth-child(n+4) { border-bottom: 0; }
  .feature-icon { height: 56px; display: flex; justify-content: center; align-items: center; gap: 12px; }
  .feature-title { margin: 6px 0 3px; font-weight: 300; font-size: 19.5px; color: var(--blue-link); }
  .feature-text { margin: 0 auto; width: 270px; font-size: 12.5px; line-height: 16px; color: #111; }
  .map-tile { width: 52px; height: 50px; background: linear-gradient(135deg, #f4c82c, #e9a91f); }

  /* Footer */
  .site-footer { left: 0; top: 867px; width: 1200px; height: 139px; background: var(--footer-bg); color: var(--footer-text); }
  .footer-col h3 { margin: 0 0 4px; font-weight: 400; font-size: 14.5px; color: #fff; }
  .footer-col p, .footer-col li { font-size: 11.5px; line-height: 16px; margin: 0; }
  .footer-col ul { list-style: none; margin: 0; padding: 0; }
  .about-col { left: 140px; top: 17px; width: 500px; }
  .read-more { color: #4aa6ec; }
  .contact-col { left: 709px; top: 17px; }
  .contact-col li { line-height: 19.5px; }
  .social-col { left: 907px; top: 17px; }
  .social-col li { display: flex; align-items: center; gap: 8px; line-height: 22.5px; }
  .social-col .social-square { width: 14px; height: 14px; }
  .bottom-bar { left: 0; top: 1006px; width: 1200px; height: 49px; background: var(--footer-bottom); color: var(--footer-text); font-size: 11.5px; }
  .copyright { left: 144px; top: 16px; display: flex; align-items: center; gap: 6px; }
  .copyright .brand-name { font-size: 14px; color: #ddd; }
  .footer-nav { right: 141px; top: 17px; }
</style>
</head>
<body>

<header class="site-header">
  <div class="abs brand"><span class="brand-mark"></span><span class="brand-name">VELUNDA</span></div>
  <nav class="abs action-tabs">
    <div class="action-tab action-tab--primary">✎ Apply</div>
    <div class="action-tab">⊕ Add</div>
    <div class="action-tab">⧉ Join</div>
  </nav>
  <div class="abs action-note">to a festival or local event</div>
  <div class="abs search-box"></div>
  <div class="abs header-social">
    <span class="social-square" style="background:#3b5998"></span>
    <span class="social-square" style="background:#35aee2"></span>
  </div>
  <div class="abs account-links"><a class="register" href="#">Register</a> &nbsp;|&nbsp; <a class="login" href="#">Login</a></div>
  <nav class="abs main-nav"><span>About Us</span><span>Features</span><span>FAQ</span><span>Blog</span><span>Press</span></nav>
</header>

<section class="abs hero">
  <div class="hero-art" role="img" aria-label="Illustrated white silhouette of a guitarist with a blue guitar over blue swirls and a city skyline"></div>
  <h1 class="abs hero-title">Peace of Mind</h1>
  <p class="abs hero-lead">Welcome to Velunda. We connect festival and event organizers with the people that make it happen.</p>
  <div class="abs hero-cta">Get Started</div>
  <div class="abs slider-tab"><span class="slider-dot slider-dot--active"></span><span class="slider-dot"></span><span class="slider-dot"></span></div>
</section>

<section class="abs feature-grid">
  <article class="feature">
    <div class="feature-icon">
      <svg width="52" height="54" viewBox="0 0 52 54"><rect x="2" y="5" width="48" height="47" rx="3" fill="#e44d3a"/><rect x="6" y="9" width="40" height="39" fill="#fff"/><rect x="16" y="1" width="20" height="8" rx="2" fill="#2e3e50"/><path d="M10 20l3 3 5-6" stroke="#27ae60" stroke-width="2.5" fill="none"/><rect x="10" y="28" width="6" height="5" fill="#bbb"/><rect x="10" y="37" width="6" height="5" fill="#bbb"/><g stroke="#aaa" stroke-width="1.5"><path d="M22 20h18M22 24h18M22 30h18M22 34h18M22 40h18"/></g></svg>
    </div>
    <h2 class="feature-title">Event Management</h2>
    <p class="feature-text">Lorem Ipsum is simply dummy text of the printing and typesetting industry.</p>
  </article>
  <article class="feature">
    <div class="feature-icon">
      <svg width="56" height="56" viewBox="0 0 56 56"><circle cx="28" cy="28" r="28" fill="#3b5a9a"/><rect x="19" y="20" width="18" height="17" rx="2" fill="#fff"/><rect x="19" y="20" width="18" height="5" fill="#d8e0ef"/><g fill="#3b5a9a"><rect x="22" y="28" width="3" height="3"/><rect x="27" y="28" width="3" height="3"/><rect x="32" y="28" width="3" height="3"/><rect x="22" y="32" width="3" height="3"/><rect x="27" y="32" width="3" height="3"/></g></svg>
    </div>
    <h2 class="feature-title">Pagebook Event Sync</h2>
    <p class="feature-text">Lorem Ipsum is simply dummy text of the printing and typesetting industry.</p>
  </article>
  <article class="feature">
    <div class="feature-icon">
      <svg width="52" height="54" viewBox="0 0 52 54"><rect x="1" y="2" width="50" height="51" rx="2" fill="#2e3e50"/><rect x="5" y="5" width="42" height="44" fill="#fff"/><rect x="8" y="9" width="14" height="11" fill="#3498db"/><g stroke="#bbb" stroke-width="1.5"><path d="M8 25h20M8 30h16M8 35h20M8 40h14"/></g><path d="M26 40l20-20 5 5-20 20-7 2z" fill="#e44d3a"/></svg>
    </div>
    <h2 class="feature-title">Contracts &amp; Reports</h2>
    <p class="feature-text">Lorem Ipsum is simply dummy text of the printing and typesetting industry.</p>
  </article>
  <article class="feature">
    <div class="feature-icon">
      <svg width="53" height="52" viewBox="0 0 53 52"><rect x="0" y="2" width="53" height="38" rx="2" fill="#dfe3e6"/><rect x="3" y="5" width="47" height="30" fill="#1aa37a"/><rect x="22" y="40" width="9" height="7" fill="#bbb"/><rect x="15" y="47" width="23" height="3" fill="#ccc"/></svg>
      <svg width="48" height="38" viewBox="0 0 48 38"><rect x="4" y="0" width="40" height="32" rx="2" fill="#2e3e50"/><rect x="7" y="3" width="34" height="26" fill="#2d9fd9"/><rect x="0" y="32" width="48" height="5" rx="2" fill="#cfd5da"/></svg>
      <svg width="34" height="52" viewBox="0 0 34 52"><rect x="0" y="0" width="34" height="52" rx="3" fill="#2e3e50"/><rect x="3" y="6" width="28" height="38" fill="#e44d3a"/><circle cx="17" cy="48" r="2" fill="#888"/></svg>
    </div>
    <h2 class="feature-title">Website Integration</h2>
    <p class="feature-text">Lorem Ipsum is simply dummy text of the printing and typesetting industry.</p>
  </article>
  <article class="feature">
    <div class="feature-icon">
      <svg width="54" height="54" viewBox="0 0 54 54"><circle cx="27" cy="27" r="26" fill="#1e88d0"/><g stroke="#fff" stroke-width="3" fill="none"><ellipse cx="27" cy="27" rx="11" ry="26"/><path d="M27 1v52M1 27h52M5 14h44M5 40h44"/></g></svg>
    </div>
    <h2 class="feature-title">Online Submissions</h2>
    <p class="feature-text">Lorem Ipsum is simply dummy text of the printing and typesetting industry.</p>
  </article>
  <article class="feature">
    <div class="feature-icon">
      <div class="map-tile" role="img" aria-label="Folded map icon with a red location pin"></div>
    </div>
    <h2 class="feature-title">Event Venue &amp; Prep</h2>
    <p class="feature-text">Lorem Ipsum is simply dummy text of the printing and typesetting industry.</p>
  </article>
</section>

<footer class="abs site-footer">
  <div class="abs footer-col about-col">
    <h3>What is Velunda?</h3>
    <p>Velunda enables festival managers to easily offload the application and transaction process, while providing stakeholders with a single dashboard for management of multiple applications and events. It reduces the impact of repetitive processes and unnecessary transactions, while providing the social media metrics to measure and enhance ROI for event sponsors.</p>
    <p class="read-more">+ Read More</p>
  </div>
  <div class="abs footer-col contact-col">
    <h3>Contact Us:</h3>
    <ul>
      <li>- hello@velunda.com</li>
      <li>- (600) - 555 - 0148</li>
      <li>- Privacy Policy</li>
      <li>- Terms &amp; Conditions</li>
    </ul>
  </div>
  <div class="abs footer-col social-col">
    <h3>Social Integration</h3>
    <ul>
      <li><span class="social-square" style="background:#222"></span>Newsletter</li>
      <li><span class="social-square" style="background:#3b5998"></span>Pagebook</li>
      <li><span class="social-square" style="background:#35aee2"></span>Chirpline</li>
      <li><span class="social-square" style="background:#1f80c9"></span>Linkwork</li>
    </ul>
  </div>
</footer>

<div class="abs bottom-bar">
  <div class="abs copyright">Copyright © 2013 <span class="brand-name">VELUNDA</span> | All Rights Reserved</div>
  <div class="abs footer-nav">Home | About Us | Features | FAQ | Blogs | Press | Contact Us</div>
</div>

</body>
</html>
```